Quimby's Yard & Garden Center Business Card Update

I need an updated Business card design for my Lawn and Garden Center. We do Landscaping installs, Lawn Mowing, Snow Removal and also have a Garden Center Retail Division. I uploaded a few of our previous business cards to give an idea of what we are starting with. The main goal of this update is to simplify and modernize the business card, not all of the services that are on the previous cards has to be on the new one but I would still like to highlight our main services. There is also a sample of our logo that Can be used in the design.

Industry/Entity Type

Landscaping

Contact Information for Business Card

Morris Quimby
Morris@Quimbysyardandgarden.example
Business (555) 201-7784
Cell (555) 318-6092

Colors

Designer to choose colors to be used in the design.

Requirements
Must have
• Services Provided :
• Landscaping
• Lawn Maintenance
• Snow Removal
• Garden Center

```html
<!DOCTYPE html>
<html lang="en">
<head>
<meta charset="utf-8">
<title>Quimby's Yard &amp; Garden Center – Business Card</title>
<link href="https://fonts.googleapis.com/css2?family=Roboto:wght@400;500;700&display=swap" rel="stylesheet">
<style>
  :root {
    --page-bg: #e9e4dc;
    --card-white: #f2f2f2;
    --card-black: #000000;
    --leaf-green: #2d5427;
    --ink: #111111;
    --paper: #ffffff;
  }
  * { margin: 0; padding: 0; box-sizing: border-box; }
  html, body { width: 900px; height: 1200px; overflow: hidden; }
  body {
    position: relative;
    background: var(--page-bg);
    font-family: "Roboto", Arial, sans-serif;
  }
  .card {
    position: absolute;
    left: 75px;
    width: 768px;
    height: 438px;
    border-radius: 20px;
    overflow: hidden;
    box-shadow: 0 6px 16px rgba(0,0,0,0.25);
  }
  .card--front { top: 133px; background: var(--card-white); }
  .card--back { top: 628px; background: var(--card-black); }

  .brand {
    position: absolute;
    display: flex;
    align-items: center;
    font-weight: 700;
    white-space: nowrap;
  }
  .brand__dot { border-radius: 50%; flex: none; }
  .card--front .brand { left: 62px; top: 152px; gap: 14px; color: var(--leaf-green); font-size: 50px; }
  .card--front .brand__dot { width: 34px; height: 34px; background: var(--leaf-green); }
  .card--back .brand { left: 0; right: 0; top: 170px; justify-content: center; gap: 26px; color: var(--paper); font-size: 100px; }
  .card--back .brand__dot { width: 66px; height: 66px; background: var(--leaf-green); }

  .contact { position: absolute; left: 362px; top: 100px; color: var(--ink); font-size: 20px; line-height: 26px; }
  .contact__name { color: var(--leaf-green); font-size: 27px; font-weight: 700; line-height: 34px; margin-bottom: 20px; }
  .contact__phones { margin-bottom: 26px; }

  .band { position: absolute; left: 0; top: 0; width: 768px; height: 438px; }
  .address {
    position: absolute; left: 0; right: 0; top: 395px;
    text-align: center; color: var(--paper); font-size: 20px; font-weight: 500;
  }

  .services {
    position: absolute; left: 0; right: 0; top: 394px;
    display: flex; justify-content: center; gap: 18px;
    color: var(--paper); font-size: 21px; font-weight: 500; list-style: none;
  }
  .services__sep { font-weight: 400; }
</style>
</head>
<body>
  <section class="card card--front" aria-label="Business card front">
    <svg class="band" viewBox="0 0 768 438" aria-hidden="true">
      <path d="M0 402 Q384 326 768 402 L768 438 L0 438 Z" fill="var(--leaf-green)"/>
    </svg>
    <div class="brand"><span class="brand__dot"></span>Quimby's</div>
    <div class="contact">
      <p class="contact__name">Morris Quimby</p>
      <div class="contact__phones">
        <p>Business (555) 201-7784</p>
        <p>Cell (555) 318-6092</p>
      </div>
      <p>Morris@Quimbysyardandgarden.example</p>
      <p>Quimbysyardandgarden.example</p>
    </div>
    <p class="address">214 Orchard Lane, Millbrook, OHO 40000</p>
  </section>

  <section class="card card--back" aria-label="Business card back">
    <div class="brand"><span class="brand__dot"></span>Quimby's</div>
    <ul class="services">
      <li>Landscaping</li><li class="services__sep">|</li>
      <li>Lawn Maintenance</li><li class="services__sep">|</li>
      <li>Snow Removal</li><li class="services__sep">|</li>
      <li>Garden Center</li>
    </ul>
  </section>
</body>
</html>
```